A business selling natural soaps online and in farmers markets. I want it to reflect local commerce and natural lifestyle. My colors are olive green and saddle brown. I want the dimensions to be 2.25 x 3.25" with matte finish.
Updates

The name of my company is Fern Hollow Soapworks, LLC

Industry/Entity Type

Business

```html
<!DOCTYPE html>
<html lang="en">
<head>
<meta charset="utf-8">
<title>Fern Hollow Soapworks – Business Card</title>
<link href="https://fonts.googleapis.com/css2?family=Questrial&display=swap" rel="stylesheet">
<style>
  :root {
    --backdrop: #e4e4e2;
    --card-light: #d6dcc7;
    --card-dark: #c3ccb0;
    --leaf-faint: #a9b492;
    --brown: #5a2e17;
    --card-shadow: rgba(40, 40, 30, 0.28);
  }
  * { margin: 0; padding: 0; box-sizing: border-box; }
  html, body {
    width: 1200px;
    height: 720px;
    overflow: hidden;
    background: var(--backdrop);
  }
  .canvas {
    width: 1200px;
    height: 720px;
    display: flex;
    align-items: center;
    justify-content: center;
  }
  .business-card {
    position: relative;
    width: 1050px;
    height: 600px;
    background: linear-gradient(135deg, var(--card-light) 0%, var(--card-dark) 100%);
    box-shadow: 0 10px 30px var(--card-shadow);
    overflow: hidden;
    font-family: "Questrial", "Century Gothic", sans-serif;
    color: var(--brown);
  }
  .leaf-decoration {
    position: absolute;
    left: 0;
    bottom: 0;
    width: 560px;
    height: 330px;
  }
  .brand-name {
    position: absolute;
    top: 110px;
    left: 0;
    right: 0;
    text-align: center;
    font-size: 58px;
    letter-spacing: 1px;
  }
  .company-block {
    position: absolute;
    left: 80px;
    top: 300px;
    text-align: right;
    font-size: 23px;
    line-height: 34px;
    letter-spacing: 1px;
  }
  .contact-block {
    position: absolute;
    right: 70px;
    top: 292px;
    text-align: right;
    letter-spacing: 1px;
  }
  .person-name { font-size: 32px; line-height: 36px; }
  .person-role { font-size: 22px; line-height: 26px; margin-bottom: 24px; }
  .contact-line { font-size: 23px; line-height: 32px; }
</style>
</head>
<body>
  <main class="canvas">
    <section class="business-card">
      <svg class="leaf-decoration" viewBox="0 0 560 330" role="img" aria-label="Faint large leaf decoration in muted olive green">
        <defs>
          <radialGradient id="leafGlow" cx="30%" cy="70%" r="70%">
            <stop offset="0%" stop-color="#a9b492" stop-opacity="0.75"/>
            <stop offset="100%" stop-color="#a9b492" stop-opacity="0"/>
          </radialGradient>
        </defs>
        <rect width="560" height="330" fill="url(#leafGlow)"/>
      </svg>

      <h1 class="brand-name">Fern Hollow Soapworks</h1>

      <div class="company-block">
        <p class="company-name">Fern Hollow Soapworks, LLC</p>
        <p class="company-web">www.FernHollowSoapworks.com</p>
      </div>

      <div class="contact-block">
        <p class="person-name">Maren Whitfield</p>
        <p class="person-role">Owner</p>
        <p class="contact-line">Tel: +1 555 210 388</p>
        <p class="contact-line">Fax: + 1 555 210 381</p>
        <p class="contact-line">maren@fernhollowsoapworks.com</p>
      </div>
    </section>
  </main>
</body>
</html>
```